Chiro Card
Bright Path Chiropractic & Wellness
Project: Chiro Card
Chiro Card -
Creative Brief
Simple
Marcus Hale
Chiropractor
812 Orvale Ave, Suite K Corbin Falls, Tx. 78245
corbinfallsspine@mailvane.com
www.corbinfallsspine.com
Please do not include my email address on the business card.

```html
<!DOCTYPE html>
<html lang="en">
<head>
<meta charset="utf-8">
<title>Bright Path Chiropractic &amp; Wellness – Stationery</title>
<link href="https://fonts.googleapis.com/css2?family=Montserrat:wght@500;700&display=swap" rel="stylesheet">
<style>
  :root {
    --brand-blue: #1b4f8c;
    --brand-green: #5ba935;
    --green-light: #8fcf5a;
    --paper: #ffffff;
    --page-bg: #ffffff;
    --frame: #d9d9d9;
    --shadow: rgba(0,0,0,0.28);
    --line: #9a9a9a;
  }
  * { box-sizing: border-box; margin: 0; padding: 0; }
  html, body { width: 1200px; height: 681px; overflow: hidden; background: var(--page-bg); }
  body { font-family: "Montserrat", Arial, sans-serif; position: relative; }

  .presentation-frame {
    position: absolute; left: 19px; top: 24px; width: 1162px; height: 629px;
    border: 2px solid var(--frame);
  }
  .sheet {
    position: absolute; background: var(--paper);
    box-shadow: 3px 4px 8px var(--shadow);
    overflow: hidden;
  }

  /* Brand lockup: name only, one colour, one weight */
  .brand {
    display: flex; align-items: center; gap: 6px; color: var(--brand-blue);
    font-weight: 700; line-height: 1; white-space: nowrap;
  }
  .brand-dot { border-radius: 50%; background: var(--brand-green); flex: none; }
  .brand-name { display: flex; flex-direction: column; white-space: nowrap; }
  .brand-name .primary { letter-spacing: 0.5px; }
  .brand-name .secondary { letter-spacing: 0.6px; margin-top: 3px; }

  .band {
    --cap: 22px;
    position: absolute; background: var(--brand-blue); color: #fff;
    display: flex; flex-direction: column; justify-content: center; align-items: center;
    font-weight: 500; text-align: center; white-space: nowrap;
  }
  .band::before, .band::after {
    content: ""; position: absolute; top: 0; bottom: 0; width: var(--cap);
    background: linear-gradient(90deg, var(--brand-green), var(--green-light), var(--brand-green));
  }
  .band::before { left: calc(-1 * var(--cap)); }
  .band::after { right: calc(-1 * var(--cap)); }

  /* Envelope front */
  .envelope-front { left: 67px; top: 110px; width: 480px; height: 202px; }
  .envelope-front .brand { position: absolute; left: 14px; top: 16px; }
  .envelope-front .brand-dot { width: 22px; height: 22px; }
  .envelope-front .primary { font-size: 17px; }
  .envelope-front .secondary { font-size: 6.5px; }
  .envelope-front .band { left: 30px; right: 30px; top: 168px; height: 22px; font-size: 7px; letter-spacing: 0.4px; }

  /* Envelope back */
  .envelope-back { left: 67px; top: 379px; width: 480px; height: 207px; }
  .envelope-back .flap { position: absolute; inset: 0; }
  .envelope-back .brand { position: absolute; left: 50%; top: 26px; transform: translateX(-50%); }
  .envelope-back .brand-dot { width: 14px; height: 14px; }
  .envelope-back .primary { font-size: 9px; }
  .envelope-back .secondary { font-size: 4px; margin-top: 2px; }

  /* Letterhead */
  .letterhead { left: 619px; top: 48px; width: 312px; height: 576px; }
  .letterhead .brand { position: absolute; left: 50%; top: 26px; transform: translateX(-50%); }
  .letterhead .brand-dot { width: 24px; height: 24px; }
  .letterhead .primary { font-size: 18px; }
  .letterhead .secondary { font-size: 6.5px; }
  .letterhead .band {
    --cap: 10px;
    left: 10px; right: 10px; top: 518px; height: 40px;
    font-size: 4.3px; gap: 4px; letter-spacing: 0.1px;
  }

  /* Business card front */
  .card-front { left: 967px; top: 149px; width: 192px; height: 108px; }
  .card-front .band { left: 0; right: 0; top: 6px; height: 32px; gap: 3px; }
  .card-front .band::before, .card-front .band::after { display: none; }
  .card-front .person-name { font-size: 7px; font-weight: 700; letter-spacing: 0.4px; }
  .card-front .person-title { font-size: 5px; letter-spacing: 0.4px; }
  .card-front .brand { position: absolute; left: 50%; top: 58px; transform: translateX(-50%); }
  .card-front .brand-dot { width: 14px; height: 14px; }
  .card-front .primary { font-size: 10px; }
  .card-front .secondary { font-size: 4px; margin-top: 2px; }

  /* Business card back */
  .card-back { left: 967px; top: 283px; width: 192px; height: 106px; display: flex; align-items: center; justify-content: center; }
  .card-back .website { color: var(--brand-blue); font-size: 6px; font-weight: 500; letter-spacing: 0.5px; text-transform: uppercase; }
</style>
</head>
<body>
  <div class="presentation-frame"></div>

  <section class="sheet envelope-front" aria-label="Envelope front">
    <div class="brand">
      <span class="brand-dot"></span>
      <span class="brand-name"><span class="primary">BRIGHT PATH</span><span class="secondary">CHIROPRACTIC &amp; WELLNESS</span></span>
    </div>
    <div class="band">812 ORVALE AVE &nbsp;|&nbsp; SUITE K &nbsp;|&nbsp; CORBIN FALLS, TX. 78245</div>
  </section>

  <section class="sheet envelope-back" aria-label="Envelope back">
    <svg class="flap" viewBox="0 0 480 207" preserveAspectRatio="none">
      <path d="M4 4 Q 30 8 150 58 Q 240 92 330 58 Q 450 8 476 4" fill="none" stroke="var(--line)" stroke-width="1.2"/>
    </svg>
    <div class="brand">
      <span class="brand-dot"></span>
      <span class="brand-name"><span class="primary">BRIGHT PATH</span><span class="secondary">CHIROPRACTIC &amp; WELLNESS</span></span>
    </div>
  </section>

  <section class="sheet letterhead" aria-label="Letterhead">
    <div class="brand">
      <span class="brand-dot"></span>
      <span class="brand-name"><span class="primary">BRIGHT PATH</span><span class="secondary">CHIROPRACTIC &amp; WELLNESS</span></span>
    </div>
    <div class="band">
      <span>812 ORVALE AVE | SUITE K | CORBIN FALLS, TX. 78245</span>
      <span>PHONE: (830) 555-0148 | CORBINFALLSSPINE@MAILVANE.COM | WWW.CORBINFALLSSPINE.COM</span>
    </div>
  </section>

  <section class="sheet card-front" aria-label="Business card front">
    <div class="band">
      <span class="person-name">MARCUS HALE</span>
      <span class="person-title">CHIROPRACTOR</span>
    </div>
    <div class="brand">
      <span class="brand-dot"></span>
      <span class="brand-name"><span class="primary">BRIGHT PATH</span><span class="secondary">CHIROPRACTIC &amp; WELLNESS</span></span>
    </div>
  </section>

  <section class="sheet card-back" aria-label="Business card back">
    <span class="website">www.corbinfallsspine.com</span>
  </section>
</body>
</html>
```